Plumhart honey labels

we are in need of new labels. we are changing to shorter round cream style honey jars. scalable from 25-100mm tall. We are looking for simple yet elegant
we sell premium varietal honeys from around the USA and locally produced small batch honeys. we are in San Francisco and Sonoma county Calif. for 10 yrs. we strive to supply only the highest quality honey at a premium price point
our logo is gold text on black background, can be found at plumhart.net

Reason: would like to see more designs for a paper wrap around label

Reason: get your designs in so we can choose soon

Target Market(s)

we provide Premium honeys that cannot be found easily elsewhere
at Premium prices. Our customers are socially aware but not afraid to pay more for a premium product

Colors

Designer to choose colors to be used in the design.

Requirements
Must have
• we will be using round jars in 3 sizes, 1.5-4 inches tall, 53mm,63mm,89mm diameter
all will have black lids
will need wrap around labels for labeling machine application
will need simple nutrition label info included
Nice to have
• room on side for nutrition label info
plumhart logo included, of course
space on side for short description of honey
Should not have
• honey dripping off honey dipper or spoon
picture of honeycomb
comic bees or flowers

```html
<!DOCTYPE html>
<html lang="en">
<head>
<meta charset="utf-8">
<title>Plumhart Honey Label</title>
<link rel="stylesheet" href="https://fonts.googleapis.com/css2?family=Josefin+Sans:wght@300;400&display=swap">
<style>
  :root {
    --backdrop: #d9d9d9;
    --label-black: #0b0b0b;
    --honey-gold: #f2b81c;
    --illustration-tone: #2a2208;
  }
  html, body {
    margin: 0;
    padding: 0;
    width: 1200px;
    height: 900px;
    overflow: hidden;
    background: var(--backdrop);
  }
  .canvas {
    position: relative;
    width: 1200px;
    height: 900px;
    background: radial-gradient(ellipse at 50% 30%, #f2f2f2 0%, var(--backdrop) 75%);
  }
  .label {
    position: absolute;
    left: 382px;
    top: 138px;
    width: 436px;
    height: 624px;
    background: var(--label-black);
    color: var(--honey-gold);
    font-family: "Josefin Sans", sans-serif;
    font-weight: 300;
  }
  .brand-name {
    position: absolute;
    top: 88px;
    left: 0;
    width: 100%;
    text-align: center;
    font-size: 50px;
    font-weight: 400;
    letter-spacing: 1px;
    margin: 0;
  }
  .meadow-illustration {
    position: absolute;
    left: 78px;
    top: 254px;
    width: 280px;
    height: 174px;
    background: linear-gradient(180deg, var(--illustration-tone) 0%, #17130a 100%);
  }
  .tagline {
    position: absolute;
    top: 434px;
    left: 0;
    width: 100%;
    text-align: center;
    font-size: 21px;
    letter-spacing: 0.5px;
    margin: 0;
  }
  .product-name {
    position: absolute;
    top: 472px;
    left: 0;
    width: 100%;
    text-align: center;
    font-size: 80px;
    letter-spacing: 1px;
    line-height: 1;
    margin: 0;
  }
  .rule {
    position: absolute;
    left: 87px;
    top: 572px;
    width: 262px;
    height: 2px;
    background: var(--honey-gold);
  }
</style>
</head>
<body>
  <main class="canvas">
    <section class="label">
      <h1 class="brand-name">plumhart</h1>
      <div class="meadow-illustration" role="img" aria-label="Line illustration of a bee flying beside a row of tall, thin-stemmed gold flowers"></div>
      <p class="tagline">RAW, UNFILTERED, PURE</p>
      <h2 class="product-name">HONEY</h2>
      <div class="rule"></div>
    </section>
  </main>
</body>
</html>
```